#28 - On the Letterheadpaper, can you please make the footercolorfields littlebit darker? I mean the Colors are too bright compared to the Logocolors, or?!
@Torven #22 - Can you please add on the backside the url's like on #7 ?
@quembrastudio #18 - Businesscard: The footer (colored fields) maybe a little bit to strong/high, can you test it with 2-3px less? #18 - Letterheadpaper: Need the footer (colored fields) here! Looks without ... nacked. ;) #18 - Please add the "Back of the business card"-things what you can read in the briefing.
@quembrastudio #1#2 - Eliminated; Better draft available with #4 #11 - Eliminated; I think the logo is better on a "normal" business card style, and maybe thats are other card Dimensions. #10 #9 - The Black Symbols on the Businesscard is maybe to strong. Can you test it with blue or grey symbols? #4 - At the moment my favorite, but please the "84116 Grunwiesel" in a new line under the Street (businesscard), thats the correct format in Germany. I'm not so happy with the URL in the blue footerfield, maybe smaller or in a other location, I don't know?! Please put on the letterhead the Facts from the footer into the header (right under the Logo), maybe in a small/tiny clear Fonttype. The Flyerbusinesscard don't have the color fields on the bottom?
@torven #8 - Front looks nice, but the Logo on the backside is not strong/"clear" enough I think. #7#5 - Eliminated; Not my Style, Sorry. #6 - Eliminated; The footer (blue field) on the Front was to heavy
Can't vote for your drafts the Flyer and Letterhead are missing.
@vOlpt
Nice blue symbols on the Businesscard, but the color on the backside is purple, I think that kills the blue/grey Logo and Style on the Frontside. And the Logo with Name under it is one unit, either the Logo with the Name direct under the Logo, or the Logo standalone. :)
Cant't vote for your drafts, don't need Envelopes but the Flyer. ;)
@Marble314
Thanks for your Drafts, but it's not my Style and I think it's not the Style from the Logo, the heavy yellow Background "kills" the nice look of the Blue/Grey Logo, too.
#2 In Germany is it more standard that the Logo is on the right side.
Please make a new draft with the Logo on the right side and the personal data (Address) under the Logo. In the footer comes the web address and maybe later some bank account informations or a funny quote.
I miss in the Address the ID and the Name of the City (I forget it in the briefing, Sorry) please add it to the drafts.
=> "84116 Grunwiesel"
The Name under the Logo ("Lukas Wendorf") looks like a little to big/wide on the right side, please let it start and end on the exact same width that the Logo is.
The "Background" of the Flyer with the integrated Business Card can't be complete blue, there will be some Text added in the future, it's a information Flyer with some facts about my work and so on, so there must be some space for these texts. The Businesscard "in" the Flyer must the same Card as the normal Business card, except the round corners.
The Dimensions from all the stuff is like the given Dimensions from the attached Information-PDF's?
OK, the price is guaranteed! I would upgrade this project, the Problem is I must pay with coinrelay, and in Germany you send via echeck the money from your regular bank account to coinrelay. But this way need very very long here on zentrofix.example (I don't know why), i paid this project on the 16. feb, today (25. fe) the project started, ~7 workdays for clearing the echeck. So, when I now pay the Guaranteed-Upgrade the project-option will confirmed when the project ends ...
The Logo itself comes from my first project here on zentrofix.example, and there was the price guaranteed, too.
#22 - Can you please add on the backside the url's like on #7 ?
@quembrastudio
#18 - Businesscard: The footer (colored fields) maybe a little bit to strong/high, can you test it with 2-3px less?
#18 - Letterheadpaper: Need the footer (colored fields) here! Looks without ... nacked. ;)
#18 - Please add the "Back of the business card"-things what you can read in the briefing.
#1 #2 - Eliminated; Better draft available with #4
#11 - Eliminated; I think the logo is better on a "normal" business card style, and maybe thats are other card Dimensions.
#10 #9 - The Black Symbols on the Businesscard is maybe to strong. Can you test it with blue or grey symbols?
#4 - At the moment my favorite, but please the "84116 Grunwiesel" in a new line under the Street (businesscard), thats the correct format in Germany. I'm not so happy with the URL in the blue footerfield, maybe smaller or in a other location, I don't know?! Please put on the letterhead the Facts from the footer into the header (right under the Logo), maybe in a small/tiny clear Fonttype. The Flyerbusinesscard don't have the color fields on the bottom?
@torven
#8 - Front looks nice, but the Logo on the backside is not strong/"clear" enough I think.
#7 #5 - Eliminated; Not my Style, Sorry.
#6 - Eliminated; The footer (blue field) on the Front was to heavy
So, trust me or not.
--- Gerold

```html
<!DOCTYPE html>
<html lang="de">
<head>
<meta charset="utf-8">
<title>Lukas Wendorf – Visitenkarten</title>
<link href="https://fonts.googleapis.com/css2?family=Cinzel:wght@400&family=PT+Sans:wght@400;700&display=swap" rel="stylesheet">
<style>
  :root {
    --stage-light: #ffffff;
    --stage-dark: #e2e2e2;
    --label-grey: #8a8a8a;
    --card-white: #ffffff;
    --brand-blue: #1f4f9c;
    --brand-blue-light: #3466b6;
    --brand-blue-deep: #183e80;
    --brand-grey: #4a4a4a;
    --card-black: #2c2c2c;
    --card-black-deep: #141414;
    --text-grey: #555555;
    --text-white: #ffffff;
    --rule-blue: #3b6cc0;
  }
  * { margin: 0; padding: 0; box-sizing: border-box; }
  html, body { width: 1200px; height: 947px; overflow: hidden; }
  body {
    position: relative;
    background: radial-gradient(ellipse at 50% 45%, var(--stage-light) 0%, #f3f3f3 50%, var(--stage-dark) 100%);
    font-family: "PT Sans", sans-serif;
  }
  .side-label {
    position: absolute;
    width: 300px;
    text-align: center;
    font-family: "Cinzel", serif;
    font-size: 34px;
    line-height: 40px;
    color: var(--label-grey);
    letter-spacing: 1px;
  }
  .card {
    position: absolute;
    overflow: hidden;
    box-shadow: 0 10px 14px -6px rgba(0,0,0,0.35), 0 1px 3px rgba(0,0,0,0.15);
  }

  /* white front */
  .card-white {
    left: 141px; top: 133px; width: 454px; height: 377px;
    background: var(--card-white);
    border: 1px solid #d6d6d6;
  }
  .holder {
    position: absolute;
    left: 30px; top: 64px; width: 180px;
  }
  .holder-name {
    font-weight: 700;
    font-size: 24px;
    line-height: 30px;
    color: var(--brand-blue);
  }
  .divider {
    position: absolute;
    left: 232px; top: 40px;
    width: 2px; height: 270px;
    background: var(--rule-blue);
  }
  .brand-block {
    position: absolute;
    left: 254px; top: 34px; width: 176px;
  }
  .brand-mark {
    width: 56px; height: 56px;
    margin-bottom: 8px;
    background: var(--brand-blue);
  }
  .brand-name {
    font-weight: 700;
    font-size: 17px;
    line-height: 22px;
    color: var(--brand-blue);
    white-space: nowrap;
    margin-bottom: 10px;
  }
  .contact-line {
    font-size: 12.5px;
    line-height: 18px;
    color: var(--text-grey);
    white-space: nowrap;
  }
  .contact-line b { color: var(--brand-blue); }
  .footer-fields {
    position: absolute;
    left: 0; bottom: 0; width: 100%; height: 32px;
    display: flex;
  }
  .footer-blue {
    flex: 3;
    background: var(--brand-blue);
    color: var(--text-white);
    font-size: 12px;
    line-height: 32px;
    padding-left: 30px;
  }
  .footer-grey { flex: 1; background: var(--brand-grey); }

  /* dark fronts */
  .card-blue {
    left: 610px; top: 133px; width: 487px; height: 377px;
    background: radial-gradient(ellipse at 50% 40%, var(--brand-blue-light) 0%, var(--brand-blue) 50%, var(--brand-blue-deep) 100%);
  }
  .card-black {
    left: 610px; top: 597px; width: 487px; height: 244px;
    background: radial-gradient(ellipse at 50% 40%, #3a3a3a 0%, var(--card-black) 45%, var(--card-black-deep) 100%);
  }
  .dark-brand {
    position: absolute;
    left: 0; width: 100%;
    text-align: center;
    font-weight: 700;
    font-size: 32px;
    line-height: 40px;
    color: var(--text-white);
  }
  .card-blue .dark-brand { top: 78px; }
  .card-black .dark-brand { top: 36px; }
  .profile-links {
    position: absolute;
    left: 148px;
    list-style: none;
    color: var(--text-white);
    font-size: 14px;
  }
  .card-blue .profile-links { top: 170px; line-height: 23px; }
  .card-black .profile-links { top: 110px; line-height: 21px; }
</style>
</head>
<body>
  <div class="side-label" style="left:218px; top:76px;">FRONT</div>
  <div class="side-label" style="left:703px; top:76px;">FRONT</div>
  <div class="side-label" style="left:703px; top:527px;">FRONT</div>

  <section class="card card-white" aria-label="Visitenkarte Vorderseite weiß">
    <div class="holder">
      <div class="holder-name">Lukas Wendorf</div>
    </div>
    <div class="divider"></div>
    <div class="brand-block">
      <div class="brand-mark"></div>
      <div class="brand-name">Lukas Wendorf</div>
      <div class="contact-line"><b>Add:</b> Lindenweg 14</div>
      <div class="contact-line">84116 Grunwiesel</div>
      <div class="contact-line"><b>P:</b> 09341 / 5528310</div>
      <div class="contact-line"><b>C:</b> 0172 / 4418207</div>
      <div class="contact-line"><b>F:</b> 09341 / 5528319</div>
      <div class="contact-line"><b>E:</b> mail@wendorflukas.example</div>
    </div>
    <div class="footer-fields">
      <div class="footer-blue">www.wendorflukas.example</div>
      <div class="footer-grey"></div>
    </div>
  </section>

  <section class="card card-blue" aria-label="Visitenkarte Vorderseite blau">
    <div class="dark-brand">Lukas Wendorf</div>
    <ul class="profile-links">
      <li>chirpline.example/JustAPlaceholder</li>
      <li>friendwall.example/JustAPlaceholder</li>
      <li>careerlink.example/JustAPlaceholder</li>
      <li>bizring.example/JustAPlaceholder</li>
    </ul>
  </section>

  <section class="card card-black" aria-label="Visitenkarte Vorderseite schwarz">
    <div class="dark-brand">Lukas Wendorf</div>
    <ul class="profile-links">
      <li>chirpline.example/JustAPlaceholder</li>
      <li>friendwall.example/JustAPlaceholder</li>
      <li>careerlink.example/JustAPlaceholder</li>
      <li>bizring.example/JustAPlaceholder</li>
    </ul>
  </section>
</body>
</html>
```